Marlene Business Card

My wife is going to start her own business with renting holiday appartments to tourists. She needs a design for a new business card... and a new web site.
Look at Roomvesta "Ruhezeit am Birkenteich"

Target Market(s)

Give business card to prospects at any situation

Contact Information for Business Card

not sure what this means

Font styles to use
Script

Colors
fec41a
fee18a

Requirements
Must have
• My wife's handwriting is difficult to read:
Entspannen - Loslassen - Auftanken
Marlene & der Birkenteich
Urlaub an einem besonderen Ort
Marlene Brökel
Gartenpfad 7
17489 Alt Medow
info@marlene-broekel.de
www.birkenteich.net
Nice to have
• Beige background
Font like handwriting

```html
<!DOCTYPE html>
<html lang="de">
<head>
<meta charset="utf-8">
<title>Marlene &amp; der Birkenteich – Visitenkarte</title>
<link rel="stylesheet" href="https://fonts.googleapis.com/css2?family=Dancing+Script:wght@500;700&display=swap">
<style>
  :root {
    --backdrop: #d6d6d6;
    --card-light: #fcebb9;
    --card-mid: #f9e3a2;
    --card-deep: #f5d88a;
    --ink: #151515;
    --accent-soft: #f6d27a;
  }
  * { margin: 0; padding: 0; box-sizing: border-box; }
  html, body {
    width: 1200px;
    height: 900px;
    overflow: hidden;
    background: var(--backdrop);
    font-family: "Dancing Script", cursive;
    color: var(--ink);
  }
  .sheet {
    position: relative;
    width: 1200px;
    height: 900px;
  }
  .card {
    position: absolute;
    left: 250px;
    width: 700px;
    height: 400px;
    border-radius: 18px;
    background: linear-gradient(160deg, var(--card-light) 0%, var(--card-mid) 55%, var(--card-deep) 100%);
    box-shadow: 0 6px 18px rgba(0,0,0,0.18);
    overflow: hidden;
  }
  .card--front { top: 35px; }
  .card--back { top: 465px; }

  .leaf-decor {
    position: absolute;
    border-radius: 50%;
    background: radial-gradient(circle, var(--accent-soft) 0%, rgba(246,210,122,0) 70%);
    opacity: 0.7;
  }
  .leaf-decor--top-left { left: 60px; top: -60px; width: 240px; height: 180px; }
  .leaf-decor--right { right: -40px; top: 90px; width: 260px; height: 240px; }
  .leaf-decor--bottom-left { left: -40px; bottom: -50px; width: 260px; height: 200px; }

  .business-name {
    position: absolute;
    left: 0;
    right: 0;
    text-align: center;
    font-weight: 700;
    white-space: nowrap;
    line-height: 1.2;
  }
  .card--front .business-name { top: 162px; font-size: 60px; }
  .card--back .business-name { top: 118px; font-size: 54px; }

  .tagline {
    position: absolute;
    top: 68px;
    left: 0;
    right: 0;
    text-align: center;
    font-size: 26px;
    font-weight: 500;
  }
  .subline {
    position: absolute;
    top: 196px;
    left: 0;
    right: 0;
    text-align: center;
    font-size: 30px;
    font-weight: 500;
  }
  .address {
    position: absolute;
    left: 40px;
    bottom: 30px;
    font-size: 24px;
    font-weight: 500;
    line-height: 1.25;
    font-style: normal;
  }
  .contact {
    position: absolute;
    right: 30px;
    bottom: 36px;
    list-style: none;
    font-size: 20px;
    font-weight: 500;
    line-height: 1.5;
  }
  .contact li {
    display: flex;
    align-items: center;
    justify-content: flex-end;
    gap: 8px;
  }
  .contact svg { width: 20px; height: 20px; }
</style>
</head>
<body>
<main class="sheet">

  <section class="card card--front" aria-label="Vorderseite">
    <div class="leaf-decor leaf-decor--top-left" role="img" aria-label="Zarte Blattzeichnung in Goldtönen"></div>
    <div class="leaf-decor leaf-decor--right" role="img" aria-label="Zarte Blattzeichnung in Goldtönen"></div>
    <div class="leaf-decor leaf-decor--bottom-left" role="img" aria-label="Zarte Blattzeichnung in Goldtönen"></div>
    <h1 class="business-name">Marlene &amp; der Birkenteich</h1>
  </section>

  <section class="card card--back" aria-label="Rückseite">
    <p class="tagline">Entspannen - Loslassen - Auftanken</p>
    <h2 class="business-name">Marlene &amp; der Birkenteich</h2>
    <p class="subline">Urlaub an einem besonderen Ort</p>

    <address class="address">
      Marlene Brökel<br>
      Gartenpfad 7<br>
      17489 Alt Medow
    </address>

    <ul class="contact">
      <li>info@marlene-broekel.de
        <svg viewBox="0 0 20 20" aria-hidden="true">
          <circle cx="10" cy="10" r="10" fill="#151515"/>
          <rect x="5" y="6.5" width="10" height="7" fill="none" stroke="#fff" stroke-width="1"/>
          <path d="M5 6.5 L10 10.5 L15 6.5" fill="none" stroke="#fff" stroke-width="1"/>
        </svg>
      </li>
      <li>www.birkenteich.net
        <svg viewBox="0 0 20 20" aria-hidden="true">
          <circle cx="10" cy="10" r="10" fill="#151515"/>
          <circle cx="10" cy="10" r="5.5" fill="none" stroke="#fff" stroke-width="1"/>
          <ellipse cx="10" cy="10" rx="2.3" ry="5.5" fill="none" stroke="#fff" stroke-width="1"/>
          <line x1="4.5" y1="10" x2="15.5" y2="10" stroke="#fff" stroke-width="1"/>
        </svg>
      </li>
    </ul>
  </section>

</main>
</body>
</html>
```